Redesign for Popular UK Town Website

We're looking for someone to redesign a website for a popular tourist town that's visited by over 250,000 people a year. We have a basic design frame in place and need someone to make it look more 'professional.'
We've created a temporary design layout to show you a general idea of what we're looking for: http://dorrin.co.uk/
All text/images are placeholder images so you can get an idea of the general layout.
(Please note that you can grab any images found on the internet for 'tenby' to be used as placeholder images. This is because we will be visiting the locations and taking our own photos, after the design is complete.)
Target Market(s)
Tourists
Industry/Entity Type
Town
Number of Pages Required
2 page
Requirements
Must have
- You need to redesign the homepage: http://dorrin.co.uk/
- You also need to redesign the following page: http://dorrin.co.uk/hotels/ (This page will be used for multiple categories and is used to list locations of properties/places etc.)
- Design must be responsive also.
Nice to have
- Please feel free to add as much as you can to the content/features as with our limited knowledge of websites, have only been able to create a basic layout.

```html
<!DOCTYPE html>
<html lang="en">
<head>
<meta charset="utf-8">
<title>Dorrin — Visit the Harbour Town</title>
<link href="https://fonts.googleapis.com/css2?family=Lato:wght@300;400;700;900&display=swap" rel="stylesheet">
<style>
:root{
  --ink:#1d1d1f;
  --white:#ffffff;
  --accent:#d8463d;
  --accent-soft:rgba(216,70,61,.82);
  --band:rgba(20,24,32,.62);
  --night:#1e2d44;
  --night-deep:#121b29;
  --footer:#000000;
  --muted:#9a9a9a;
  --sea:#1bb3b0;
  --sky:#3b6fd0;
}
*{margin:0;padding:0;box-sizing:border-box}
html,body{width:1200px;height:4176px;overflow:hidden}
body{position:relative;background:var(--white);font-family:'Lato',sans-serif;color:var(--ink)}
.abs{position:absolute}
.photo{position:absolute}

/* hero */
.hero{left:0;top:0;width:1200px;height:880px;background:linear-gradient(180deg,#4d8fd0 0%,#8fc6d9 14%,#24a9a6 30%,#1f9c8a 55%,#2d8a5c 70%,#19a7a3 100%)}
.brand{left:56px;top:10px;display:flex;align-items:center;gap:16px}
.brand-mark{width:120px;height:120px;border-radius:50%;border:5px solid var(--white)}
.brand-name{color:var(--white);font-weight:700;font-size:30px;letter-spacing:2px}
.nav{left:222px;top:36px;display:flex;gap:22px;align-items:center}
.nav a{color:var(--white);text-decoration:none;font-size:14px;font-weight:700;letter-spacing:.4px;text-transform:uppercase}
.nav .phone{background:var(--white);color:var(--ink);border-radius:6px;padding:8px 14px;font-size:14px;margin-left:26px}
.slide-arrow{width:84px;height:84px;top:356px;border:3px solid rgba(255,255,255,.85);border-radius:50%}
.hero-kicker{left:0;width:1200px;top:540px;text-align:center;color:var(--white);font-size:18px;font-weight:700;letter-spacing:1px}
.hero-title{left:0;width:1200px;top:580px;text-align:center;color:var(--white);font-size:68px;font-weight:700;letter-spacing:1px}
.hero-text{left:360px;width:480px;top:686px;text-align:center;color:var(--white);font-size:18px;font-weight:700;line-height:22px}
.dots{left:0;width:1200px;top:814px;display:flex;justify-content:center;gap:10px}
.dots span{width:12px;height:12px;border-radius:50%;background:rgba(255,255,255,.6)}
.dots span.on{background:var(--white)}

/* section headings */
.sec-title{left:0;width:1200px;text-align:center;font-size:26px;font-weight:400;letter-spacing:.5px}
.sec-sub{left:0;width:1200px;text-align:center;font-size:11px;color:var(--accent);letter-spacing:.6px;text-transform:uppercase}

/* offers */
.offer{width:400px;height:328px}
.offer-label{left:0;right:0;bottom:0;height:74px;background:var(--band);color:var(--white);font-size:20px;padding:28px 0 0 18px;text-transform:uppercase}
.offer-label.book{background:var(--accent-soft);display:flex;justify-content:space-between;padding-right:18px}
.more-info{left:0;right:0;top:100px;text-align:center;color:var(--white);font-size:19px;text-transform:uppercase}
.more-info b{display:block;font-size:52px;font-weight:300;line-height:52px}
.deal{right:18px;top:4px;width:130px;height:64px;background:var(--accent);color:var(--white);text-align:center;font-size:11px;padding-top:12px;text-transform:uppercase}
.deal strong{display:block;font-size:21px;font-weight:400;margin-top:4px}

/* sights */
.sights{left:0;top:1851px;width:1200px;height:905px;background:linear-gradient(180deg,#1c2f55 0%,#2a4b74 40%,#5a5848 75%,#3a3228 100%)}
.sight-img{width:342px;height:230px}
.sight-btn{width:317px;height:68px;background:rgba(190,180,150,.42);border:2px solid rgba(255,255,255,.35);color:var(--white);font-size:24px;text-align:center;line-height:64px}

/* news */
.news{left:0;top:2756px;width:1200px;height:1036px;background:linear-gradient(180deg,#1b2836 0%,#101a20 100%)}
.news .sec-title,.news .sec-sub{color:var(--white)}
.news .sec-title{font-weight:700}
.tile{width:266px;height:376px}
.tile-label{left:0;right:0;top:168px;text-align:center;color:var(--white);font-size:27px}
.tile.active .tile-label{top:auto;bottom:18px;text-align:left;padding-left:24px}
.tile-plus{left:0;right:0;top:140px;text-align:center;color:var(--white);font-size:56px;font-weight:300}

/* footer */
.footer{left:0;top:3792px;width:1200px;height:328px;background:var(--footer);color:var(--white)}
.f-head{font-size:14px;text-transform:uppercase;letter-spacing:.4px}
.f-list{list-style:none;font-size:14px;font-weight:700}
.f-contact li{display:flex;gap:14px;margin-bottom:18px;line-height:18px}
.f-contact svg{flex:none;margin-top:2px}
.f-links li{margin-bottom:20px;text-transform:uppercase}
.tweets{left:827px;top:72px;width:240px;height:160px;background:var(--white);color:var(--ink);border-radius:3px;padding:10px 12px;font-size:10px}
.tweets h4{font-size:17px;font-weight:400}
.tweets h4 small{font-size:10px;color:#3b88c3}
.tweet-row{display:flex;gap:8px;margin-top:10px}
.tweet-dot{width:22px;height:22px;background:#cfd5dc;border-radius:3px;flex:none}
.tweet-foot{left:12px;right:12px;bottom:10px;height:8px;background:#3b88c3}
.bottom{left:0;top:4120px;width:1200px;height:56px;background:var(--white)}
.socials{left:156px;top:22px;display:flex;gap:16px}
.socials span{width:13px;height:13px;border-radius:50%;background:var(--muted)}
.copyright{right:150px;top:22px;font-size:10px;color:var(--muted);text-transform:uppercase}
</style>
</head>
<body>

<header class="hero abs" role="img" aria-label="Aerial photograph of the harbour town, turquoise sea, green headland and colourful houses">
</header>
<div class="brand abs"><span class="brand-mark"></span><span class="brand-name">DORRIN</span></div>
<nav class="nav abs">
  <a href="#">Where to stay</a><a href="#">Caravans and camping</a><a href="#">Bed and breakfast</a><a href="#">Hotels in Dorrin</a><a href="#">Contact</a>
  <a class="phone" href="#">44-2000-555-010</a>
</nav>
<div class="slide-arrow abs" style="left:102px">
  <svg width="78" height="78" viewBox="0 0 78 78"><path d="M44 26 L31 39 L44 52" fill="none" stroke="#fff" stroke-width="3"/></svg>
</div>
<div class="slide-arrow abs" style="left:1032px">
  <svg width="78" height="78" viewBox="0 0 78 78"><path d="M34 26 L47 39 L34 52" fill="none" stroke="#fff" stroke-width="3"/></svg>
</div>
<p class="hero-kicker abs">DORRIN</p>
<h1 class="hero-title abs">THE HARBOUR</h1>
<p class="hero-text abs">Scenic and serene - the harbour in Dorrin boasts wonders of Nature found in few places around the world. Beautiful cove with amazing tides.</p>
<div class="dots abs"><span></span><span></span><span class="on"></span><span class="on"></span></div>

<h2 class="sec-title abs" style="top:944px">BEST OFFERS</h2>
<p class="sec-sub abs" style="top:982px">Hotel, camping and bed offers in Dorrin</p>

<div class="offer abs" style="left:0;top:1038px">
  <div class="photo" style="inset:0;background:linear-gradient(180deg,#3f64c9,#a9b7ea 45%,#6f7fc8 70%,#3a4a68)" role="img" aria-label="Wide harbour view under a streaked blue sky"></div>
  <div class="offer-label abs">The Harbour</div>
</div>
<div class="offer abs" style="left:400px;top:1038px">
  <div class="photo" style="inset:0;background:linear-gradient(180deg,#3e78d8,#a7c4e8 35%,#d9cdb4 55%,#3c5a68)" role="img" aria-label="Colourful seafront houses above a small harbour with boats"></div>
  <div class="offer-label abs">Water Sports</div>
</div>
<div class="offer abs" style="left:800px;top:1038px">
  <div class="photo" style="inset:0;background:linear-gradient(180deg,#6aa3d8,#23b0ad 40%,#3f8a53 65%,#1ea5a0)" role="img" aria-label="Aerial view of turquoise bay and green headland"></div>
  <div class="offer-label abs">Parasailing</div>
</div>
<div class="offer abs" style="left:0;top:1366px">
  <div class="photo" style="inset:0;background:linear-gradient(180deg,#8a8a8a,#3a3a3a 55%,#1c1c1c)" role="img" aria-label="Black and white photo of a hotel entrance with railings"></div>
  <div class="more-info abs"><b>+</b>More info</div>
  <div class="offer-label book abs"><span>Marlowe Hotel</span><span style="text-transform:none">Book Now</span></div>
</div>
<div class="offer abs" style="left:400px;top:1366px">
  <div class="photo" style="inset:0;background:linear-gradient(180deg,#2f4fb8,#6d7fd0 45%,#7a6a9a 60%,#1f2e6a)" role="img" aria-label="Castle ruins reflected in a lake at dusk"></div>
  <div class="offer-label abs">Harlow Castle</div>
</div>
<div class="offer abs" style="left:800px;top:1366px">
  <div class="photo" style="inset:0;background:linear-gradient(180deg,#2f58c6,#b0bde8 45%,#6d86c2 70%,#2a3e66)" role="img" aria-label="Town skyline and beach under a blue sky"></div>
  <div class="deal abs">Best in Dorrin<strong>25% OFF</strong></div>
  <div class="offer-label abs">Summer Getaways</div>
</div>

<h2 class="sec-title abs" style="top:1746px">SITES AND SIGHTSEEING</h2>
<p class="sec-sub abs" style="top:1784px">Places to see and things to do</p>

<section class="sights abs" role="img" aria-label="Dimmed coastal panorama background">
</section>
<div class="sight-img photo" style="left:33px;top:1988px;background:linear-gradient(180deg,#3f64c9,#b1bdeb 50%,#4b5a80)" role="img" aria-label="Beach under streaked sky"></div>
<div class="sight-btn abs" style="left:45px;top:2244px">Top 10 Beaches</div>
<div class="sight-img photo" style="left:429px;top:1988px;background:linear-gradient(180deg,#3e78d8,#c8d6e6 40%,#d9cdb4 60%,#3c5a68)" role="img" aria-label="Harbour houses at night-out district"></div>
<div class="sight-btn abs" style="left:441px;top:2244px">Top 5 Night-Clubs</div>
<div class="sight-img photo" style="left:821px;top:1988px;background:linear-gradient(180deg,#6aa3d8,#23b0ad 40%,#3f8a53 70%)" role="img" aria-label="Aerial view of coastal hotels"></div>
<div class="sight-btn abs" style="left:833px;top:2244px">Top Hotels</div>
<div class="sight-img photo" style="left:33px;top:2347px;background:linear-gradient(180deg,#9a9a9a,#3a3a3a 60%,#1c1c1c)" role="img" aria-label="Black and white entrance of a building"></div>
<div class="sight-btn abs" style="left:45px;top:2603px">Top Caravan Sites</div>
<div class="sight-img photo" style="left:429px;top:2347px;background:linear-gradient(180deg,#2f4fb8,#6d7fd0 50%,#1f2e6a)" role="img" aria-label="Lakeside castle at dusk"></div>
<div class="sight-btn abs" style="left:441px;top:2603px">Places To Eat</div>
<div class="sight-img photo" style="left:821px;top:2347px;background:linear-gradient(180deg,#2f58c6,#b0bde8 50%,#2a3e66)" role="img" aria-label="Town skyline by the sea"></div>
<div class="sight-btn abs" style="left:833px;top:2603px">Cultural Sites</div>

<section class="news abs" role="img" aria-label="Dark aerial town background">
</section>
<h2 class="sec-title abs" style="top:2815px;color:#fff;font-weight:700">NEWS FROM DORRIN</h2>
<p class="sec-sub abs" style="top:2853px;color:#fff;text-transform:none;font-style:italic">Latest news and promotions</p>

<div class="tile active abs" style="left:11px;top:2923px">
  <div class="photo" style="inset:0;background:linear-gradient(180deg,#4d88d8,#7a9ac0 50%,#5f8a4a 85%)" role="img" aria-label="Castle tower ruin with cannon"></div>
  <div class="tile-plus abs">+</div><div class="tile-label abs">Harlow Castle</div>
</div>
<div class="tile abs" style="left:309px;top:2923px">
  <div class="photo" style="inset:0;background:linear-gradient(180deg,#3b4552,#4a5a62 45%,#6a6250 80%,#3a3128)" role="img" aria-label="Sandy beach seen from a cliff"></div>
  <div class="tile-label abs">Shell Beach</div>
</div>
<div class="tile abs" style="left:607px;top:2923px">
  <div class="photo" style="inset:0;background:linear-gradient(180deg,#2a3c55,#4a5060 50%,#4b5a30 85%)" role="img" aria-label="Castle tower ruin"></div>
  <div class="tile-label abs">Harlow Castle</div>
</div>
<div class="tile abs" style="left:902px;top:2923px">
  <div class="photo" style="inset:0;background:linear-gradient(180deg,#3b4552,#4a5a62 45%,#6a6250 80%,#3a3128)" role="img" aria-label="Sandy beach seen from a cliff"></div>
  <div class="tile-label abs">Shell Beach</div>
</div>
<div class="tile abs" style="left:11px;top:3321px">
  <div class="photo" style="inset:0;background:linear-gradient(180deg,#3b4552,#4a5a62 45%,#6a6250 80%,#3a3128)" role="img" aria-label="Sandy beach seen from a cliff"></div>
  <div class="tile-label abs">Shell Beach</div>
</div>
<div class="tile abs" style="left:309px;top:3321px">
  <div class="photo" style="inset:0;background:linear-gradient(180deg,#3a4048,#2e3034 50%,#1a1b1d)" role="img" aria-label="Round stone gate tower with arches"></div>
  <div class="tile-label abs">Old Gate</div>
</div>
<div class="tile abs" style="left:607px;top:3321px">
  <div class="photo" style="inset:0;background:linear-gradient(180deg,#3b4552,#4a5a62 45%,#6a6250 80%,#3a3128)" role="img" aria-label="Sandy beach seen from a cliff"></div>
  <div class="tile-label abs">Shell Beach</div>
</div>
<div class="tile abs" style="left:902px;top:3321px">
  <div class="photo" style="inset:0;background:linear-gradient(180deg,#3a4048,#2e3034 50%,#1a1b1d)" role="img" aria-label="Round stone gate tower with arches"></div>
  <div class="tile-label abs">Old Gate</div>
</div>

<footer class="footer abs">
  <h3 class="f-head abs" style="left:150px;top:50px">Sponsored space</h3>
  <h3 class="f-head abs" style="left:373px;top:50px">Contact info</h3>
  <ul class="f-list f-contact abs" style="left:373px;top:90px">
    <li><svg width="10" height="14" viewBox="0 0 10 14"><path d="M5 0a5 5 0 0 1 5 5c0 4-5 9-5 9S0 9 0 5a5 5 0 0 1 5-5z" fill="#fff"/></svg><span>City Hall<br>Dorrin-On-Sea<br>Wales</span></li>
    <li><svg width="10" height="14" viewBox="0 0 10 14"><rect x="1" y="0" width="8" height="14" rx="2" fill="#fff"/></svg>44-2000-555-021</li>
    <li><svg width="10" height="14" viewBox="0 0 10 14"><path d="M2 1l2 3-1 2c1 2 2 3 4 4l2-1 1 3-2 1C4 12 0 7 1 3z" fill="#fff"/></svg>44-2000-555-032</li>
    <li><svg width="12" height="10" viewBox="0 0 12 10"><rect width="12" height="10" fill="#fff"/><path d="M0 0l6 5 6-5" fill="none" stroke="#000"/></svg>info@dorrin.co.uk</li>
    <li><svg width="12" height="12" viewBox="0 0 12 12"><circle cx="6" cy="6" r="6" fill="#fff"/></svg>www.dorrin.co.uk</li>
  </ul>
  <h3 class="f-head abs" style="left:601px;top:50px">Things to do</h3>
  <ul class="f-list f-links abs" style="left:601px;top:96px">
    <li>Culture fair</li><li>Art galleries</li><li>Hikes</li><li>Extreme sports</li>
  </ul>
  <h3 class="f-head abs" style="left:827px;top:50px">Social</h3>
  <div class="tweets abs">
    <h4>Tweets <small>by @DorrinOfficial</small></h4>
    <div class="tweet-row"><span class="tweet-dot"></span><span>Visit Dorrin Official<br>Retweeted</span></div>
    <div class="tweet-row"><span class="tweet-dot"></span><span><b>Wander With Jo</b><br>The Westmoor coastline is stunning today</span></div>
    <div class="tweet-foot abs"></div>
  </div>
</footer>
<div class="bottom abs">
  <div class="socials abs"><span></span><span></span><span></span><span></span><span></span><span></span><span></span><span></span></div>
  <p class="copyright abs">2015 Copyright all rights reserved dorrin.co.uk</p>
</div>

</body>
</html>
```